Clean Stylish Hip Online Marketplace Website Design

I am needing a seasoned designer with a hipster flair to design an online marketplace that connects people with others who can provide home and professional baking services in their local area. Need maps, feature driven and above all an identifiable LOOK to the site that is clean, trustworthy and inviting. (Online Marketplace service like Quillrest, Tamblo.com, CraftHerdz but with the look of Wanderlattebook.com, Zipo, holbeckinn.com)

Target Market(s)

Women, special occasion hosts, Moms, Bride-to-be

Industry/Entity Type

Marketplace

Number of Pages Required

5+ page

Font styles to use
Serif
Sans Serif

Requirements
Must have
• Modern, subtle feminine elements, hip. 2 options for user on home page similar to craft herdz 1) Become a OvenNest 2) Post or Search For Your Dessert. ABOUT, Categories (list of baked goods), Browse Projects, How it works, Log in. Profile set up page and profile of bakers with their uploaded photos of their baked items. Post for a project page where user can go it in request all bakers in the area for a baked good. Name, City Baked good,Date/Time needed, Description of Project and submit button. List of all the projects where bakers can accept or decline project with a bid. Payment Page.
Nice to have
• Map capabilities somewhere for people to filter down by location. Be able to showcase bakers cake or cookies photos in a beautiful unique and stylish way.
Should not have
• Nothing too girly or corporate. I am looking for a very stylized website for an online marketplace.

```html
<!DOCTYPE html>
<html lang="en">
<head>
<meta charset="utf-8">
<title>OvenNest.com – Preview Local Bakers</title>
<link href="https://fonts.googleapis.com/css2?family=Jost:wght@400;500&family=Montserrat:wght@500&family=Open+Sans:wght@400;600;700&display=swap" rel="stylesheet">
<style>
  :root {
    --ink: #111111;
    --black: #000000;
    --white: #ffffff;
    --panel: rgba(226, 226, 226, 0.92);
    --band: rgba(222, 222, 222, 0.92);
    --accent: #e5323b;
    --bg-top: #f4f2ef;
    --bg-bottom: #e9e6e1;
  }
  * { box-sizing: border-box; margin: 0; padding: 0; }
  html, body { width: 1200px; height: 576px; overflow: hidden; }
  body { font-family: "Open Sans", Arial, sans-serif; color: var(--ink); }
  h1, h2, h3 { font-weight: 400; }

  .page {
    position: relative;
    width: 1200px;
    height: 576px;
    overflow: hidden;
    background: linear-gradient(160deg, var(--bg-top) 0%, #efebe6 45%, var(--bg-bottom) 100%);
  }
  .page-backdrop {
    position: absolute; inset: 0;
    background: radial-gradient(ellipse at 78% 20%, rgba(214, 204, 190, 0.55), transparent 55%),
                radial-gradient(ellipse at 12% 70%, rgba(220, 212, 200, 0.5), transparent 50%);
  }

  /* header */
  .brand {
    position: absolute; left: 161px; top: 14px;
    display: flex; align-items: center;
  }
  .brand-name {
    font-family: "Jost", Arial, sans-serif; font-weight: 500;
    font-size: 22px; letter-spacing: 2px; color: var(--ink);
    padding-right: 12px; border-right: 1px solid #9a9a9a; line-height: 28px;
  }
  .brand-tagline {
    font-family: "Jost", Arial, sans-serif; font-size: 12px;
    padding-left: 11px; color: var(--ink);
  }

  /* toolbar */
  .toolbar {
    position: absolute; left: 161px; top: 64px; width: 877px; height: 47px;
    background: var(--black); display: flex; align-items: center;
  }
  .toolbar-title {
    font-family: "Jost", Arial, sans-serif; font-size: 17px; color: var(--white);
    letter-spacing: 0.6px; margin-left: 19px; flex: 1;
  }
  .search { display: flex; height: 29px; margin-right: 9px; }
  .search-field {
    width: 248px; background: var(--white); font-size: 9.5px; color: #8a8a8a;
    display: flex; align-items: center; padding-left: 11px;
  }
  .search-button {
    width: 80px; background: var(--accent); color: var(--white);
    font-family: "Jost", Arial, sans-serif; font-size: 10.5px;
    display: flex; align-items: center; justify-content: center;
  }

  .section-title {
    position: absolute; left: 174px; top: 121px;
    font-family: "Jost", Arial, sans-serif; font-size: 16.5px; letter-spacing: 0.4px;
  }

  /* baker cards */
  .baker-card { position: absolute; left: 162px; width: 876px; height: 157px; }
  .baker-card--first { top: 157px; }
  .baker-card--second { top: 323px; }
  .baker-portrait { position: absolute; left: 0; top: 0; width: 149px; height: 157px; }
  .baker-info { position: absolute; left: 149px; top: 0; width: 405px; height: 157px; background: var(--panel); }
  .baker-gallery-item { position: absolute; top: 0; height: 157px; }

  .baker-name {
    position: absolute; left: 20px; top: 11px;
    font-family: "Jost", Arial, sans-serif; font-size: 16.5px; letter-spacing: 0.8px;
  }
  .baker-motto { position: absolute; left: 20px; top: 37px; font-size: 9.5px; }
  .label {
    font-family: "Jost", Arial, sans-serif; font-size: 13.5px; letter-spacing: 0.2px;
  }
  .baker-experience { position: absolute; left: 20px; top: 67px; }
  .baker-detail { position: absolute; left: 20px; font-size: 9.5px; }
  .baker-reviews { position: absolute; left: 240px; top: 10px; display: flex; align-items: center; gap: 14px; }
  .stars { display: flex; }
  .baker-specialties { position: absolute; left: 240px; top: 36px; }
  .specialty-list { position: absolute; left: 240px; top: 58px; font-size: 9.5px; line-height: 17.5px; white-space: nowrap; }
  .details-button {
    position: absolute; left: 241px; width: 100px; height: 22px;
    background: var(--black); color: var(--white); font-weight: 700; font-size: 9.5px;
    display: flex; align-items: center; justify-content: center; letter-spacing: 0.2px;
  }

  /* call to action */
  .cta { position: absolute; left: 162px; top: 488px; width: 876px; height: 47px; }
  .cta-question {
    position: absolute; left: 0; top: 0; width: 620px; height: 47px; background: var(--band);
    font-family: "Montserrat", Arial, sans-serif; font-weight: 500; font-size: 18.5px;
    display: flex; align-items: center; padding-left: 11px;
  }
  .cta-shape { position: absolute; left: 599px; top: 0; }
  .cta-label {
    position: absolute; left: 599px; top: 0; width: 277px; height: 47px;
    color: var(--white); font-family: "Jost", Arial, sans-serif; font-size: 16.5px;
    letter-spacing: 0.5px; display: flex; align-items: center; justify-content: center; padding-left: 26px;
  }

  .footer-note { position: absolute; left: 162px; top: 551px; font-family: "Montserrat", Arial, sans-serif; font-size: 8px; color: #333; }
  .page-code { position: absolute; left: 1061px; top: 548px; font-family: "Montserrat", Arial, sans-serif; font-size: 8.5px; }
</style>
</head>
<body>
<div class="page">
  <div class="page-backdrop" role="img" aria-label="Softly faded background photo of flour sacks and grain on a white wooden table"></div>

  <header class="brand">
    <span class="brand-name">OVENNEST.COM</span>
    <span class="brand-tagline">Bringing Local Bakers to You</span>
  </header>

  <div class="toolbar">
    <h1 class="toolbar-title">PREVIEW LOCAL BAKERS</h1>
    <div class="search">
      <div class="search-field">Search for Backers, Specialty, Location , etc...</div>
      <div class="search-button">SEARCH</div>
    </div>
  </div>

  <h2 class="section-title">POST OR SEARCH FOR A DESSERT</h2>

  <article class="baker-card baker-card--first">
    <div class="baker-portrait" role="img" aria-label="Portrait photo of Corwin, a smiling baker in a green shirt" style="background: linear-gradient(160deg, #3a2a22 0%, #6b5448 45%, #4d8a3c 100%);"></div>
    <div class="baker-info">
      <h3 class="baker-name">CORWIN M.</h3>
      <p class="baker-motto">Good Things Come to Those that Bake...</p>
      <p class="label baker-experience">EXPERIENCE LEVEL</p>
      <p class="baker-detail" style="top:91px;">Home Baker (years) or Professional</p>
      <p class="baker-detail" style="top:110px;">Alder Row, Marrow Bay, WA, 98101</p>
      <div class="baker-reviews">
        <span class="label">REVIEWS</span>
        <svg class="stars" width="80" height="12" viewBox="0 0 80 12" aria-label="4 out of 5 stars">
          <g fill="var(--accent)" stroke="var(--accent)" stroke-width="0.8">
            <polygon points="6,0.6 7.6,4.2 11.4,4.5 8.5,7 9.4,10.8 6,8.8 2.6,10.8 3.5,7 0.6,4.5 4.4,4.2"/>
            <polygon transform="translate(17 0)" points="6,0.6 7.6,4.2 11.4,4.5 8.5,7 9.4,10.8 6,8.8 2.6,10.8 3.5,7 0.6,4.5 4.4,4.2"/>
            <polygon transform="translate(34 0)" points="6,0.6 7.6,4.2 11.4,4.5 8.5,7 9.4,10.8 6,8.8 2.6,10.8 3.5,7 0.6,4.5 4.4,4.2"/>
            <polygon transform="translate(51 0)" points="6,0.6 7.6,4.2 11.4,4.5 8.5,7 9.4,10.8 6,8.8 2.6,10.8 3.5,7 0.6,4.5 4.4,4.2"/>
            <polygon transform="translate(68 0)" fill="none" points="6,0.6 7.6,4.2 11.4,4.5 8.5,7 9.4,10.8 6,8.8 2.6,10.8 3.5,7 0.6,4.5 4.4,4.2"/>
          </g>
        </svg>
      </div>
      <p class="label baker-specialties">SPECIALTIES</p>
      <p class="specialty-list">Cupcakes, Cakes, Pies,<br>Pastries, Cake Pops, Cookies,<br>Gluten Free, Nut Fee</p>
      <div class="details-button" style="top:118px;">MORE DETAILS</div>
    </div>
    <div class="baker-gallery-item" role="img" aria-label="Photo of pastries and berry-topped cakes on a cooling rack" style="left:559px; width:317px; background: linear-gradient(135deg, #3a2418 0%, #8a4a2a 40%, #d98a8a 70%, #e8b070 100%);"></div>
  </article>

  <article class="baker-card baker-card--second">
    <div class="baker-portrait" role="img" aria-label="Portrait photo of Liora, a baker in a black hat and light coat" style="background: linear-gradient(160deg, #f2f2f2 0%, #dcd2c8 50%, #2a2220 100%);"></div>
    <div class="baker-info">
      <h3 class="baker-name">LIORA S.</h3>
      <p class="baker-motto">Stop hating. Start Baking &lt;3</p>
      <p class="label baker-experience">EXPERIENCE LEVEL</p>
      <p class="baker-detail" style="top:91px;">&nbsp;Professional</p>
      <p class="baker-detail" style="top:110px;">Fennick, WA, 98029</p>
      <div class="baker-reviews">
        <span class="label">REVIEWS</span>
        <svg class="stars" width="80" height="12" viewBox="0 0 80 12" aria-label="4 out of 5 stars">
          <g fill="var(--accent)" stroke="var(--accent)" stroke-width="0.8">
            <polygon points="6,0.6 7.6,4.2 11.4,4.5 8.5,7 9.4,10.8 6,8.8 2.6,10.8 3.5,7 0.6,4.5 4.4,4.2"/>
            <polygon transform="translate(17 0)" points="6,0.6 7.6,4.2 11.4,4.5 8.5,7 9.4,10.8 6,8.8 2.6,10.8 3.5,7 0.6,4.5 4.4,4.2"/>
            <polygon transform="translate(34 0)" points="6,0.6 7.6,4.2 11.4,4.5 8.5,7 9.4,10.8 6,8.8 2.6,10.8 3.5,7 0.6,4.5 4.4,4.2"/>
            <polygon transform="translate(51 0)" points="6,0.6 7.6,4.2 11.4,4.5 8.5,7 9.4,10.8 6,8.8 2.6,10.8 3.5,7 0.6,4.5 4.4,4.2"/>
            <polygon transform="translate(68 0)" fill="none" points="6,0.6 7.6,4.2 11.4,4.5 8.5,7 9.4,10.8 6,8.8 2.6,10.8 3.5,7 0.6,4.5 4.4,4.2"/>
          </g>
        </svg>
      </div>
      <p class="label baker-specialties">SPECIALTIES</p>
      <p class="specialty-list">Cupcakes, Cakes, Cake Pops,<br>Cookies</p>
      <div class="details-button" style="top:109px;">MORE DETAILS</div>
    </div>
    <div class="baker-gallery-item" role="img" aria-label="Photo of a frosted cupcake with a candy cane and red bow" style="left:559px; width:159px; background: linear-gradient(180deg, #cfd0d3 0%, #e6e6e8 60%, #d8dadd 100%);"></div>
    <div class="baker-gallery-item" role="img" aria-label="Close-up photo of pink and white frosted cupcakes with sprinkles" style="left:724px; width:152px; background: linear-gradient(135deg, #e88a72 0%, #f3c0b0 45%, #f4ece8 75%, #e8a090 100%);"></div>
  </article>

  <div class="cta">
    <p class="cta-question">Can’t Find Exactly What You Need?</p>
    <svg class="cta-shape" width="277" height="47" viewBox="0 0 277 47" aria-hidden="true">
      <polygon points="0,0 277,0 277,47 0,47 27,23.5" fill="var(--black)"/>
    </svg>
    <p class="cta-label">POST YOUR PROJECT</p>
  </div>

  <footer class="footer-note">© 2016 .www.ovennest.com &nbsp;|&nbsp; All Rights Reserved.</footer>
  <span class="page-code">M1</span>
</div>
</body>
</html>
```